"Landing Page Design for Premium Eco-Friendly Laundry Strips – Plooifris.nl"

We need a visually appealing and high-converting landing page for our premium laundry strips, emphasizing luxury, sustainability, and ease of use. The page should include sections such as:

Hero Section: A compelling introduction with a strong headline, subheadline, and a clear call-to-action (CTA).
Product Benefits: Highlighting key features like eco-friendliness, long-lasting scent, and hypoallergenic qualities.
Product Description: Focusing on innovation and sustainability.
How It Works: Simple, visual steps for using the product.
Customer Reviews: Authentic testimonials to build trust and social proof.
FAQ Section: Addressing common concerns about the product.
The design should maintain a luxurious aesthetic while ensuring clarity and user-friendliness. We also offer free shipping on all orders, a key differentiator to be prominently displayed. All texts and translations are already provided for implementation. Please deliver the design in Figma format."

Target Market(s)

"Eco-conscious consumers and families seeking premium and sustainable laundry solutions. Target age group: 25-50, predominantly women who prioritize luxury and environmental impact."

Industry/Entity Type

"Laundry care and eco-friendly consumer goods."

Coding

Requirements
Must have
• A visually luxurious design emphasizing premium quality and eco-friendliness. Clear call-to-actions (e.g., 'Try Now – Free Shipping'). Sections for product benefits, how it works, customer reviews, and FAQ. Highlight free shipping with no minimum order prominently."
Nice to have
• Elegant, minimalist animations to enhance the premium feel. Subtle use of gold and black to emphasize luxury, with a touch of green for sustainability. Interactive customer reviews section (e.g., carousel or testimonials)."
Should not have
• Overly cluttered designs or overwhelming text blocks. Generic stock photos not aligned with our brand identity. Bright or overly playful color schemes that detract from the premium feel."

```html
<!DOCTYPE html>
<html lang="nl">
<head>
<meta charset="utf-8">
<title>Plooifris – Premium Wasstrips</title>
<link href="https://fonts.googleapis.com/css2?family=Lexend:wght@300;400;500;600&family=Montserrat:wght@400;500;600;700&display=swap" rel="stylesheet">
<style>
:root{
  --gold:#c9a13a;
  --gold-light:#e6c65a;
  --gold-dark:#b3862a;
  --black:#0b0b0b;
  --ink:#1a1a1a;
  --text:#333;
  --cream:#f5f1ea;
  --line:#ecdca8;
  --white:#fff;
}
*{box-sizing:border-box;margin:0;padding:0}
html,body{width:1200px;height:4598px;overflow:hidden}
body{position:relative;background:var(--white);font-family:"Montserrat",sans-serif;color:var(--text)}
.abs{position:absolute}
h1,h2,h3{font-family:"Lexend",sans-serif;font-weight:400;color:var(--ink)}
.btn{position:absolute;display:flex;align-items:center;justify-content:center;font-family:"Montserrat",sans-serif;font-weight:700;font-size:16px;color:#fff;text-decoration:none;white-space:nowrap}
.btn-gold{background:linear-gradient(90deg,var(--gold-dark),var(--gold-light))}
.btn-black{background:var(--black)}
.rule{position:absolute;height:3px;width:80px;background:var(--gold);left:560px}

/* nav */
.nav{position:absolute;top:0;left:0;width:1200px;height:84px;z-index:3}
.brand{position:absolute;display:flex;align-items:center;gap:12px;font-family:"Lexend",sans-serif;font-size:28px;color:var(--gold)}
.brand i{width:42px;height:42px;border-radius:50%;background:var(--gold);display:block}
.nav-links{position:absolute;left:400px;top:32px;display:flex;font-size:14px;font-weight:500;color:var(--ink);white-space:nowrap}
.nav-links span{padding:0 14px;border-right:1px solid #c8c0b0;line-height:16px}
.nav-links span:last-child{border:none}

/* hero */
.hero{position:absolute;top:0;left:0;width:1200px;height:720px;background:linear-gradient(90deg,#f7f4ef 0%,#efe9e0 60%,#e8e0d4 100%)}
.hero-photo{position:absolute;left:540px;top:90px;width:660px;height:560px;background:radial-gradient(ellipse at 60% 60%,#c7a77a 0%,#d9c7ab 40%,rgba(232,224,212,0) 72%)}
.hero h1{position:absolute;left:116px;top:168px;font-size:52px;line-height:56px}
.hero h1 .gold{color:var(--gold)}
.hero p{position:absolute;left:118px;top:350px;width:440px;font-size:15px;line-height:21px;color:var(--ink)}
.ship{position:absolute;left:124px;top:485px;font-size:15px;color:var(--ink);display:flex;align-items:center;gap:6px}

/* benefits */
.benefits h2{position:absolute;top:772px;width:1200px;text-align:center;font-size:32px}
.orn-ring{position:absolute;left:410px;top:870px;width:380px;height:380px;border-radius:50%;border:2px solid #f1e6c6}
.orn{position:absolute;left:470px;top:930px;width:260px;height:260px;border-radius:50%;background:radial-gradient(circle,#e3c15a,#b9892c 70%,rgba(255,255,255,0) 71%)}
.ico{position:absolute;width:86px;height:86px;border-radius:50%;background:var(--black);display:flex;align-items:center;justify-content:center}
.feat{position:absolute;width:300px;font-size:15px;line-height:19px;color:var(--ink)}
.feat b{display:block;font-weight:700;font-size:16px;margin-bottom:4px}
.feat.l{text-align:right}

/* product story */
.story-photo{position:absolute;left:0;top:1406px;width:588px;height:566px;background:linear-gradient(135deg,#cdbfae,#e9e0d3 55%,#bfae98)}
.story{position:absolute;left:588px;top:1406px;width:612px;height:566px;background:linear-gradient(120deg,#e5c25a,#c9972f 60%,#b8862a)}
.story h2{position:absolute;left:98px;top:104px;font-size:38px;line-height:44px;color:#fff}
.story .bar{position:absolute;left:100px;top:200px;width:56px;height:3px;background:#fff}
.story p{position:absolute;left:100px;top:228px;width:440px;font-size:17px;line-height:28px;color:#fff}

/* steps */
.steps h2{position:absolute;top:2090px;width:1200px;text-align:center;font-size:38px}
.step{position:absolute;width:240px;text-align:center}
.step .disc{margin:0 auto;width:140px;height:140px;border-radius:50%;border:2px solid var(--gold);padding:5px;position:relative}
.step .disc div{width:100%;height:100%;border-radius:50%;background:var(--black)}
.step .num{position:absolute;left:6px;bottom:4px;width:26px;height:26px;border-radius:50%;background:var(--gold);color:#fff;font-size:14px;font-weight:700;display:flex;align-items:center;justify-content:center}
.step p{margin-top:18px;font-weight:700;font-size:17px;line-height:22px;color:var(--ink)}
.dash{position:absolute;top:2258px;width:70px;height:20px}

/* reviews */
.reviews{position:absolute;top:2632px;left:0;width:1200px;height:528px;background:radial-gradient(ellipse at 50% 40%,#1a1712,#050505 70%)}
.reviews h2{position:absolute;top:72px;width:1200px;text-align:center;font-size:38px;color:#fff}
.card{position:absolute;top:183px;width:417px;height:210px;background:linear-gradient(135deg,#e3c05a,#c4932f);padding:6px}
.card div{width:100%;height:100%;border:2px solid #f3df9d;text-align:center;color:#fff;font-size:18px;line-height:22px;padding:40px 30px 0}
.card .stars{font-size:20px;letter-spacing:2px;margin-bottom:8px}

/* faq */
.faq h2{position:absolute;top:3232px;width:1200px;text-align:center;font-size:38px}
.q{position:absolute;left:196px;width:799px;border:2px solid var(--line);background:#fff;padding:0 52px}
.q h3{font-family:"Montserrat",sans-serif;font-size:18px;font-weight:500;margin-top:28px}
.q p{font-size:14px;line-height:19px;margin-top:22px;width:630px;color:var(--ink)}
.q .tog{position:absolute;right:24px;top:26px;width:26px;height:26px;border-radius:50%;background:var(--gold);color:#fff;font-weight:700;display:flex;align-items:center;justify-content:center;font-size:18px}

/* cta + footer */
.footer{position:absolute;top:4124px;left:0;width:1200px;height:474px;background:var(--black)}
.cta-frame{position:absolute;left:137px;top:3890px;width:925px;height:380px;border:2px solid var(--gold-light)}
.cta{position:absolute;left:148px;top:3900px;width:902px;height:360px;background:linear-gradient(120deg,#e6c55c,#c89630 70%)}
.cta h2{position:absolute;top:30px;width:902px;text-align:center;font-size:32px;line-height:40px;color:#fff}
.cta .btn{left:298px;top:180px;width:306px;height:52px;border:2px solid #fff;font-size:15px}
.fcol{position:absolute;top:4290px;font-size:15px;color:#fff}
.fcol h3{font-family:"Lexend",sans-serif;color:var(--gold-light);font-size:22px;margin-bottom:22px}
.fcol span{display:block;margin-bottom:20px}
.soc{display:flex;gap:12px;margin-top:20px}
.soc i{width:36px;height:36px;border-radius:50%;background:var(--gold-light);display:block}
.copy{position:absolute;top:4556px;width:1200px;text-align:center;font-size:13px;color:#8a8a8a}
.fline{position:absolute;top:4528px;left:148px;width:904px;height:1px;background:#2a2a2a}
</style>
</head>
<body>

<section class="hero">
  <div class="hero-photo" role="img" aria-label="Productdoos met wasstrips naast een rieten wasmand met gevouwen kleding"></div>
  <svg class="abs" style="left:0;top:600px" width="1200" height="130" viewBox="0 0 1200 130">
    <path d="M0 110 C300 20 700 40 1200 100 L1200 130 L0 130Z" fill="#fff"/>
    <path d="M0 110 C300 20 700 40 1200 100" stroke="#d2a83c" stroke-width="8" fill="none"/>
  </svg>
  <h1><span class="gold">Ervaar Luxe en</span><br>Duurzaamheid in<br>Elke Wasbeurt</h1>
  <p>Ontdek de premium wasstrips van Plooifris – waar verfijning en ecologisch bewustzijn samenkomen</p>
  <a class="btn btn-gold" style="left:120px;top:423px;width:163px;height:42px">Probeer Nu ›</a>
  <svg class="abs" style="left:300px;top:420px" width="240" height="80" viewBox="0 0 240 80"><path d="M0 20 C60 -10 110 10 120 40 C130 70 190 70 222 68" stroke="#d2a83c" stroke-dasharray="4 4" fill="none"/><path d="M218 62 L228 68 L216 72Z" fill="#d2a83c"/></svg>
  <div class="ship">
    <svg width="24" height="14" viewBox="0 0 24 14"><rect x="1" y="2" width="13" height="8" fill="none" stroke="#333" stroke-width="1.5"/><path d="M14 5 H19 L22 8 V10 H14" fill="none" stroke="#333" stroke-width="1.5"/><circle cx="5" cy="11" r="2" fill="#333"/><circle cx="18" cy="11" r="2" fill="#333"/></svg>
    Altijd Gratis Verzending!
  </div>
</section>

<nav class="nav">
  <div class="brand" style="left:100px;top:20px"><i></i>PLOOIFRIS</div>
  <div class="nav-links"><span>Voordelen</span><span>Product</span><span>Hoe het werkt</span><span>Beoordelingen</span><span>FAQ</span></div>
  <a class="btn btn-gold" style="left:958px;top:24px;width:124px;height:36px;font-weight:500;font-size:15px">Probeer nu</a>
</nav>

<section class="benefits">
  <h2>Waarom Kiezen Voor Plooifris Wasstrips?</h2>
  <div class="rule" style="top:826px"></div>
  <div class="orn-ring"></div>
  <div class="orn" role="img" aria-label="Gouden bloemornament"></div>

  <div class="feat l" style="left:105px;top:890px"><b>Milieuvriendelijk</b>100% biologisch afbreekbaar en plasticvrij.</div>
  <div class="ico" style="left:434px;top:886px"><svg width="40" height="40" viewBox="0 0 40 40"><path d="M10 30 C10 14 22 8 32 8 C32 22 24 32 10 30Z M10 30 L24 16" stroke="#d2a83c" stroke-width="2" fill="none"/></svg></div>
  <div class="feat l" style="left:32px;top:1035px"><b>Langdurige Geur</b>Een heerlijke frisse geur die dagenlang blijft hangen.</div>
  <div class="ico" style="left:363px;top:1022px"><svg width="40" height="40" viewBox="0 0 40 40"><path d="M13 32 C8 24 18 20 13 8 M21 32 C16 24 26 20 21 8 M29 32 C24 24 34 20 29 8" stroke="#d2a83c" stroke-width="2" fill="none"/></svg></div>
  <div class="feat l" style="left:105px;top:1188px"><b>Geschikt voor Alle Stoffen</b>Veilig voor fijne was, wit, kleur en zwart.</div>
  <div class="ico" style="left:432px;top:1172px"><svg width="40" height="40" viewBox="0 0 40 40"><rect x="9" y="14" width="22" height="18" stroke="#d2a83c" stroke-width="2" fill="none"/><circle cx="20" cy="10" r="4" stroke="#d2a83c" stroke-width="2" fill="none"/></svg></div>

  <div class="feat" style="left:798px;top:890px"><b>Hypoallergeen</b>Perfect voor de gevoelige huid en babykleding.</div>
  <div class="ico" style="left:694px;top:892px"><svg width="40" height="40" viewBox="0 0 40 40"><path d="M12 10 L17 8 C18 11 22 11 23 8 L28 10 L33 16 L28 19 V32 H12 V19 L7 16Z" stroke="#d2a83c" stroke-width="2" fill="none"/></svg></div>
  <div class="feat" style="left:870px;top:1022px"><b>Compact en<br>Gebruiksvriendelijk</b>Geen gedoe met zware flessen – scheur, voeg toe en geniet.</div>
  <div class="ico" style="left:764px;top:1022px"><svg width="40" height="40" viewBox="0 0 40 40"><path d="M14 12 C10 18 8 21 8 24 A6 6 0 0 0 20 24 C20 21 18 18 14 12Z M27 8 C24 13 23 15 23 17 A4 4 0 0 0 31 17 C31 15 30 13 27 8Z" stroke="#d2a83c" stroke-width="2" fill="none"/></svg></div>
  <div class="feat" style="left:798px;top:1198px"><b>Altijd Gratis Verzending</b>Geen minimale bestelhoeveelheid vereist.</div>
  <div class="ico" style="left:692px;top:1184px"><svg width="44" height="40" viewBox="0 0 44 40"><rect x="4" y="10" width="22" height="16" stroke="#d2a83c" stroke-width="2" fill="none"/><path d="M26 15 H34 L40 21 V26 H26" stroke="#d2a83c" stroke-width="2" fill="none"/><circle cx="11" cy="29" r="3" fill="#d2a83c"/><circle cx="33" cy="29" r="3" fill="#d2a83c"/></svg></div>
</section>

<div class="story-photo" role="img" aria-label="Productdoos met wasstrips op een steen voor beige zijden stof"></div>
<section class="story">
  <h2>De Toekomst van<br>Wassen Is Hier</h2>
  <div class="bar"></div>
  <p>Onze Plooifris Wasstrips combineren innovatie met duurzaamheid. Met slechts één strip per wasbeurt geniet je van een schone en heerlijk geurende was, zonder het milieu te belasten. Geen plastic flessen, geen verspilling – alleen pure waskracht in een handige strip.</p>
  <a class="btn btn-black" style="left:102px;top:426px;width:170px;height:46px;font-size:15px">Probeer Nu ›</a>
</section>

<section class="steps">
  <h2>Zo Gebruik Je Wasstrips</h2>
  <div class="rule" style="top:2146px;width:64px;left:568px"></div>
  <div class="step" style="left:94px;top:2200px"><div class="disc"><div role="img" aria-label="Strip afscheuren"></div><span class="num">1</span></div><p>Scheur een<br>wasstrip af</p></div>
  <div class="step" style="left:352px;top:2200px"><div class="disc"><div role="img" aria-label="Strip in de trommel"></div><span class="num">2</span></div><p>Plaats de strip direct<br>in de trommel,<br>samen met je</p></div>
  <div class="step" style="left:610px;top:2200px"><div class="disc"><div role="img" aria-label="Wasmachine starten"></div><span class="num">3</span></div><p>Start de wasmachine<br>en laat de wasstrip<br>zijn werk doen.</p></div>
  <div class="step" style="left:874px;top:2200px"><div class="disc"><div role="img" aria-label="Schone kleding"></div><span class="num">4</span></div><p>Geniet van perfect<br>schone en fris<br>ruikende kleding!</p></div>
  <svg class="dash" style="left:312px" viewBox="0 0 70 20"><path d="M0 14 C20 0 45 0 64 14" stroke="#d2a83c" stroke-dasharray="3 3" fill="none"/></svg>
  <svg class="dash" style="left:574px;top:2280px" viewBox="0 0 70 20"><path d="M0 6 C20 20 45 20 64 6" stroke="#d2a83c" stroke-dasharray="3 3" fill="none"/></svg>
  <svg class="dash" style="left:840px" viewBox="0 0 70 20"><path d="M0 14 C20 0 45 0 64 14" stroke="#d2a83c" stroke-dasharray="3 3" fill="none"/></svg>
  <a class="btn btn-gold" style="left:455px;top:2500px;width:288px;height:55px;font-size:17px">Shop Nu – Vanaf €14,95</a>
</section>

<section class="reviews">
  <h2>Wat Onze Klanten Zeggen</h2>
  <div class="rule" style="top:128px;width:60px;left:570px"></div>
  <svg class="abs" style="left:110px;top:228px" width="26" height="50" viewBox="0 0 26 50"><path d="M22 2 L4 25 L22 48" stroke="#d2a83c" stroke-width="3" fill="none"/></svg>
  <div class="card" style="left:186px"><div><p class="stars">★★★★★</p>“Sinds ik Plooifris gebruik, voelt mijn was frisser en luxueuzer aan dan ooit.”<br>– Lotte</div></div>
  <div class="card" style="left:628px"><div><p class="stars">★★★★★</p>“Eindelijk een milieuvriendelijk product dat echt werkt en heerlijk ruikt.”<br>– Daan</div></div>
  <svg class="abs" style="left:1094px;top:228px" width="26" height="50" viewBox="0 0 26 50"><path d="M4 2 L22 25 L4 48" stroke="#d2a83c" stroke-width="3" fill="none"/></svg>
</section>

<section class="faq">
  <h2>Heb Je Nog Vragen?</h2>
  <div class="q" style="top:3335px;height:158px"><h3>Zijn de wasstrips geschikt voor mensen met een gevoelige huid?</h3><p>Ja, onze wasstrips zijn hypoallergeen en dermatologisch getest, waardoor ze veilig zijn voor de gevoelige huid.</p><span class="tog">–</span></div>
  <div class="q" style="top:3513px;height:70px"><h3 style="margin-top:22px">Hoeveel wasbeurten bevat één verpakking?</h3><span class="tog" style="top:22px">+</span></div>
  <div class="q" style="top:3591px;height:71px"><h3 style="margin-top:22px">Werken de strips bij lage temperaturen?</h3><span class="tog" style="top:22px">+</span></div>
  <a class="btn btn-black" style="left:413px;top:3718px;width:399px;height:60px">Bekijk Onze FAQ Voor Meer Antwoorden ›</a>
</section>

<footer class="footer"></footer>
<div class="cta-frame"></div>
<section class="cta">
  <h2>Start Vandaag Met Milieuvriendelijk<br>Wassen Geen Plastic, Geen Gedoe.<br><span style="font-weight:300">Alleen Fris Wassen</span></h2>
  <a class="btn">Bestel Nu – Maak Het Verschil! ›</a>
</section>

<div class="brand" style="left:140px;top:4300px;flex-direction:column;gap:14px;font-size:26px"><i style="width:110px;height:110px"></i>PLOOIFRIS</div>
<div class="fcol" style="left:400px"><h3>Navigatie</h3><span>Voordelen</span><span>Product</span><span>Hoe het werkt</span></div>
<div class="fcol" style="left:615px"><h3>Bronnen</h3><span>Beoordelingen</span><span>FAQ</span><span>Probeer het nu</span></div>
<div class="fcol" style="left:840px"><h3>Contact opnemen</h3>
  <div style="display:flex;gap:12px;align-items:center;font-size:13px;line-height:18px"><i style="width:36px;height:36px;border-radius:50%;background:var(--gold-light);display:block"></i><span style="margin:0">Stuur ons een e-mail<br>info@plooifris.nl</span></div>
  <div class="soc"><i></i><i></i><i></i><i></i></div>
</div>
<div class="fline"></div>
<p class="copy">Copyright © 2024 Wasstrips. Alle rechten voorbehouden.</p>

</body>
</html>
```